Can you make a cool and versatile Talvern Ridge Powerpoint template?
See www.talvernridge.co.uk and http://www.linkedin.com/company/talvern-ridge-ltd/ (on the right) to see how the logos are currently used - with interchangeably white and black backgrounds.
Target Market(s)
Marketing managers, product managers in HR technology, HR consultants
Industry/Entity Type
It Company
Font styles to use
Sans Serif
Requirements
Must have
- Master slide design, fonts, color theme, etc. Ideally two variations - one with white background (using colorful logo), one with a darker background (using black/white logo).

```html
<!DOCTYPE html>
<html lang="en">
<head>
<meta charset="utf-8">
<title>Talvern Ridge – Presentation Template</title>
<link rel="stylesheet" href="https://fonts.googleapis.com/css2?family=PT+Sans:wght@400;700&display=swap">
<style>
  :root {
    --canvas: #ffffff;
    --ink: #1a1a1a;
    --ink-soft: #444444;
    --brand-blue: #2a79c4;
    --accent-cyan: #29a8e0;
    --accent-green: #7cb740;
    --footer-magenta: #9b1f68;
    --row-a: #e3efd9;
    --row-b: #eff6ea;
    --frame: #c9c9c9;
    --chart-blue: #1f3fb5;
    --chart-orange: #f0561c;
    --chart-green: #8ccc3a;
    --chart-magenta: #b5166b;
  }
  * { box-sizing: border-box; margin: 0; padding: 0; }
  html, body { width: 1200px; height: 738px; overflow: hidden; background: var(--canvas); }
  body { position: relative; font-family: "PT Sans", sans-serif; color: var(--ink); }

  .slide {
    position: absolute; width: 376px; height: 284px; background: #fff;
    border: 1px solid var(--frame); box-shadow: 2px 3px 5px rgba(0,0,0,.28); overflow: hidden;
  }
  .slide--title   { left: 16px;  top: 75px; }
  .slide--bullets { left: 406px; top: 75px; }
  .slide--chart   { left: 800px; top: 75px; width: 381px; }
  .slide--table   { left: 16px;  top: 393px; width: 379px; }
  .slide--closing { left: 408px; top: 393px; width: 378px; }

  /* wordmark */
  .wordmark { position: absolute; display: flex; align-items: center; gap: 5px; color: var(--ink-soft); }
  .wordmark__dot { width: 9px; height: 9px; border-radius: 50%; background: var(--accent-cyan); }
  .wordmark--large { left: 12px; top: 30px; font-size: 12px; }
  .wordmark--large .wordmark__dot { width: 12px; height: 12px; }
  .wordmark--small { right: 10px; bottom: 16px; font-size: 7.5px; gap: 3px; }
  .wordmark--small .wordmark__dot { width: 7px; height: 7px; }

  /* photo bands */
  .band { position: absolute; height: 37px; box-shadow: 1px 2px 3px rgba(0,0,0,.25); }
  .band--blue    { background: linear-gradient(90deg, #0d3a8a, #2a8fe0 55%, #9fd6f5); }
  .band--orange  { background: linear-gradient(90deg, #3a1406, #c9580b 40%, #f4a21a 75%, #f7c55a); }
  .band--green   { background: linear-gradient(90deg, #4d5a05, #a6b80f 45%, #d6df3c); }
  .band--magenta { background: linear-gradient(90deg, #8a1a5c, #c0447f 50%, #efc3d6); }

  .cover-title { position: absolute; left: 11px; font-size: 17px; color: var(--ink); }
  .cover-sub { position: absolute; left: 11px; font-size: 11.5px; color: var(--accent-cyan); }

  /* content slide header */
  .header-photo { position: absolute; left: 0; top: 0; width: 105px; height: 46px;
    background: linear-gradient(90deg, #2f7fd2, #7cbcef 60%, #bfe1f8); }
  .header-bar { position: absolute; left: 108px; right: 0; top: 0; height: 46px; background: var(--brand-blue);
    color: #fff; font-size: 17px; display: flex; align-items: center; justify-content: flex-end; padding-right: 10px; }

  .footer { position: absolute; left: 0; right: 0; bottom: 0; height: 9px; background: var(--footer-magenta);
    color: #fff; font-size: 5px; display: flex; align-items: center; justify-content: space-between; padding: 0 8px; }

  /* bullets */
  .bullets { position: absolute; list-style: none; }
  .bullets li { position: relative; padding-left: 14px; }
  .bullets li::before { content: "•"; position: absolute; left: 0; color: var(--accent-green); }
  .bullets li.sub { padding-left: 34px; }
  .bullets li.sub::before { content: "–"; left: 18px; }
  .bullets--wide { left: 11px; top: 51px; width: 360px; font-size: 11.2px; line-height: 1.15; }
  .bullets--wide li { margin-bottom: 7px; }
  .bullets--narrow { left: 10px; top: 53px; width: 150px; font-size: 8.6px; line-height: 1.4; }
  .bullets--narrow li { margin-bottom: 7px; }

  /* chart */
  .chart-box { position: absolute; left: 178px; top: 59px; width: 193px; height: 177px; border: 1px dashed var(--accent-green); }
  .chart-title { text-align: center; font-size: 10px; margin-top: 6px; }
  .chart-box svg { position: absolute; left: 0; top: 0; }
  .chart-label { font-family: "PT Sans", sans-serif; font-size: 8.5px; fill: #fff; text-anchor: middle; }

  /* table */
  .table-title { position: absolute; left: 0; right: 0; top: 51px; text-align: center; color: var(--accent-green); font-size: 11.5px; }
  .table-intro { position: absolute; left: 10px; top: 70px; width: 355px; font-size: 9.2px; line-height: 1.45; }
  .data-table { position: absolute; left: 55px; top: 117px; border-collapse: separate; border-spacing: 1px; font-size: 8.6px; }
  .data-table th { background: var(--accent-green); color: #fff; font-weight: 400; width: 55px; height: 15px; }
  .data-table td { text-align: center; height: 15px; }
  .data-table tbody tr:nth-child(odd) td { background: var(--row-a); }
  .data-table tbody tr:nth-child(even) td { background: var(--row-b); }
</style>
</head>
<body>

<section class="slide slide--title">
  <div class="wordmark wordmark--large"><span class="wordmark__dot"></span>Talvern Ridge</div>
  <div class="band band--blue" role="img" aria-label="Dandelion seeds photo in blue tones" style="left:0;top:61px;width:312px"></div>
  <div class="band band--orange" role="img" aria-label="Dandelion seeds photo in orange tones" style="left:74px;top:103px;width:302px"></div>
  <div class="band band--green" role="img" aria-label="Dandelion seeds photo in green tones" style="left:0;top:144px;width:300px"></div>
  <div class="band band--magenta" role="img" aria-label="Dandelion seeds photo in magenta tones" style="left:85px;top:186px;width:291px"></div>
  <h1 class="cover-title" style="top:231px;font-weight:400">Presentation Title</h1>
  <p class="cover-sub" style="top:256px">Mauris ac justo a magna hendrerit</p>
</section>

<section class="slide slide--bullets">
  <div class="header-photo" role="img" aria-label="Dandelion seeds photo in blue tones"></div>
  <h2 class="header-bar" style="font-weight:400">Lorem ipsum dolor sit amet elit</h2>
  <ul class="bullets bullets--wide">
    <li>Aenean nec mollis velit. Vestibulum ante ipsum primis in faucibus orci luctus et ultrices posuere cubilia Curae.</li>
    <li>Maecenas facilisis magna sed arcu vehicula vestibulum. Donec non urna lectus.</li>
    <li>Etiam luctus feugiat diam non interdum. Aliquam dictum felis nec iaculis consectetur.</li>
    <li class="sub">Quisque eros dui, lobortis ut egestas at, aliquam vitae neque. Etiam nec luctus ante, tincidunt pharetra lacus.</li>
    <li class="sub">Aliquam eu arcu et enim viverra pretium. Mauris eu ligula pellentesque enim tristique malesuada fringilla a tortor. Nullam vel cursus metus.</li>
    <li>Phasellus vel urna vitae quam sollicitudin lacinia. Integer dolor lorem, feugiat in ligula in, vulputate dictum nisi.</li>
  </ul>
  <div class="wordmark wordmark--small"><span class="wordmark__dot"></span>Talvern Ridge</div>
  <footer class="footer"><span>13-11-2013</span><span>Confidential</span><span>2</span></footer>
</section>

<section class="slide slide--chart">
  <div class="header-photo" role="img" aria-label="Dandelion seeds photo in blue tones"></div>
  <h2 class="header-bar" style="font-weight:400">Nullam vel cursus metus</h2>
  <ul class="bullets bullets--narrow">
    <li>Phasellus vel urna vitae quam sollicitudin lacinia. Integer dolor lorem, feugiat in ligula in, vulputate dictum nisi.</li>
    <li>Proin rhoncus massa dui, non sodales libero auctor et.</li>
    <li>Duis volutpat pharetra ornare. Cras purus arcu, imperdiet et nunc et, semper ultrices turpis.</li>
    <li>Sed varius feugiat orci. Nulla sed ante a tortor viverra interdum id sed metus.</li>
  </ul>
  <div class="chart-box">
    <p class="chart-title">Graphic Title</p>
    <svg width="193" height="177" viewBox="0 0 193 177">
      <g transform="translate(92 96)">
        <path d="M0 -58 A58 58 0 1 1 -29.8 49.8 L-17.5 29.2 A34 34 0 1 0 0 -34 Z" fill="var(--chart-blue)"/>
        <path d="M-29.8 49.8 A58 58 0 0 1 -53.3 -22.8 L-31.3 -13.3 A34 34 0 0 0 -17.5 29.2 Z" fill="var(--chart-orange)"/>
        <path d="M-53.3 -22.8 A58 58 0 0 1 -29.8 -49.8 L-17.5 -29.2 A34 34 0 0 0 -31.3 -13.3 Z" fill="var(--chart-green)"/>
        <path d="M-29.8 -49.8 A58 58 0 0 1 0 -58 L0 -34 A34 34 0 0 0 -17.5 -29.2 Z" fill="var(--chart-magenta)"/>
        <text class="chart-label" x="47" y="15">8,2</text>
        <text class="chart-label" x="-46" y="16">3,2</text>
        <text class="chart-label" x="-39" y="-28">1,4</text>
        <text class="chart-label" x="-15" y="-44">1,2</text>
      </g>
    </svg>
  </div>
  <div class="wordmark wordmark--small"><span class="wordmark__dot"></span>Talvern Ridge</div>
  <footer class="footer"><span>13-11-2013</span><span>Confidential</span><span>3</span></footer>
</section>

<section class="slide slide--table">
  <div class="header-photo" role="img" aria-label="Dandelion seeds photo in blue tones"></div>
  <h2 class="header-bar" style="font-weight:400">Nullam vel cursus metus</h2>
  <p class="table-title">Table title</p>
  <p class="table-intro">Quisque eros dui, lobortis ut egestas at, aliquam vitae neque. Etiam nec luctus ante, tincidunt pharetra lacus.</p>
  <table class="data-table">
    <thead><tr><th>Category A</th><th>Category B</th><th>Category C</th><th>Category D</th><th>Category E</th></tr></thead>
    <tbody>
      <tr><td>111.222</td><td>222.333</td><td>333.444</td><td>444.555</td><td>555.666</td></tr>
      <tr><td>222.333</td><td>111.222</td><td>444.555</td><td>999.111</td><td>777.888</td></tr>
      <tr><td>333.444</td><td>777.888</td><td>222.333</td><td>111.222</td><td>444.555</td></tr>
      <tr><td>444.555</td><td>888.666</td><td>555.666</td><td>222.333</td><td>999.111</td></tr>
      <tr><td>555.666</td><td>999.111</td><td>888.666</td><td>777.888</td><td>111.222</td></tr>
    </tbody>
  </table>
  <div class="wordmark wordmark--small"><span class="wordmark__dot"></span>Talvern Ridge</div>
  <footer class="footer"><span>13-11-2013</span><span>Confidential</span><span>4</span></footer>
</section>

<section class="slide slide--closing">
  <div class="wordmark wordmark--large"><span class="wordmark__dot"></span>Talvern Ridge</div>
  <div class="band band--blue" role="img" aria-label="Dandelion seeds photo in blue tones" style="left:0;top:61px;width:312px"></div>
  <div class="band band--orange" role="img" aria-label="Dandelion seeds photo in orange tones" style="left:75px;top:104px;width:303px"></div>
  <div class="band band--green" role="img" aria-label="Dandelion seeds photo in green tones" style="left:0;top:146px;width:302px"></div>
  <div class="band band--magenta" role="img" aria-label="Dandelion seeds photo in magenta tones" style="left:86px;top:187px;width:292px"></div>
  <h1 class="cover-title" style="top:232px;font-size:16px;font-weight:400">THANK YOU</h1>
  <p class="cover-sub" style="top:257px;font-size:11px">FOR YOUR TIME</p>
</section>

</body>
</html>
```